New young doctors office business card

Doctor's office
Hello:
My name is Dr. Mateo Anselmo Quiroga Benítez. I need a business card for my new office located within a hospital. The name of the hospital is "Hospital Almendral". Although the hospital logo and name must be included in the business card, please make me a personal logo for myself. The logo might be maybe my name in a stylish font, or my initials (MAQB) or something like that. Im more inclined to a font logo, rather than a image logo, but a good one might change my mind. The info on my business card is going to be in spanish. The following info must be included please (the info within parenthesis is not to be included, it is provided for you to understand it since it's in spanish, so you can properly place it on the card):
-Dr. Mateo Anselmo Quiroga Benítez (my name)
-Medicina general (My specialty)
-Hospital Almendral (The name of the hospital where my office is)
-Calle Tomás Ibarrola #527 Col. Peñascal (address)
-Tel 471-5836 (Office phone)
-Sábado y domingo 10:00 am a 10:00pm (Office hours)
-Emergencias: 613-907-5148 (Emergency phone)
-mateoqb@correoandino.net (email)
-English Spoken
So, that's all the info i need to be on the business card. Although it's a business card for a doctor's office, i dont want it to be a boring, plain business card. Make it eye-catchy and stylish please. As i said, the hospital logo must be included. You'll find it on the heading of the PDF file i attached, but dont make it the center of attention.
Physician
Hello:My name is Dr. Mateo Anselmo Quiroga Benítez. I need a business card for my new office located within a hospital. The name of the hospital is "Hospital Almendral". Although the hospital logo and name must be included in the business card, please make me a personal logo for myself. The logo might be maybe my name in a stylish font, or my initials (MAQB) or something like that. Im more inclined to a font logo, rather than a image logo, but a good one might change my mind. The info on my business card is going to be in spanish. The following info must be included please (the info within parenthesis is not to be included, it is provided for you to understand it since it's in spanish, so you can properly place it on the card):-Dr. Mateo Anselmo Quiroga Benítez (my name)-Medicina general (My specialty)-Hospital Almendral (The name of the hospital where my office is)-Calle Tomás Ibarrola #527 Col. Peñascal (address)-Tel 471-5836 (Office phone)-Sábado y domingo 10:00 am a 10:00pm (Office hours)-Emergencias: 613-907-5148 (Emergency phone)-mateoqb@correoandino.net (email)-English Spoken So, that's all the info i need to be on the business card. Although it's a business card for a doctor's office, i dont want it to be a boring, plain business card. Make it eye-catchy and stylish please. As i said, the hospital logo must be included. You'll find it on the heading of the PDF file i attached, but dont make it the center of attention.

```html
<!DOCTYPE html>
<html lang="es">
<head>
<meta charset="utf-8">
<title>Tarjeta de presentación · Dr. Mateo Anselmo Quiroga Benítez</title>
<link rel="stylesheet" href="https://fonts.googleapis.com/css2?family=Roboto+Slab:wght@700&family=Arimo:wght@400;700&display=swap">
<style>
  :root {
    --backdrop: #d9d9d9;
    --card-navy: #1f2d70;
    --card-text: #ffffff;
    --accent-yellow: #e8e62a;
    --seal-white: #ffffff;
  }
  * { box-sizing: border-box; margin: 0; padding: 0; }
  html, body {
    width: 1200px;
    height: 900px;
    overflow: hidden;
    background: var(--backdrop);
  }
  .canvas {
    position: relative;
    width: 1200px;
    height: 900px;
  }
  .card {
    position: absolute;
    top: 140px;
    width: 350px;
    height: 620px;
    background: var(--card-navy);
    box-shadow: 0 10px 24px rgba(0,0,0,0.25);
    color: var(--card-text);
    font-family: "Arimo", Arial, sans-serif;
  }
  .card-front { left: 200px; }
  .card-back { left: 650px; }

  .hospital-seal {
    position: absolute;
    left: 50%;
    top: 50%;
    width: 200px;
    height: 200px;
    margin: -100px 0 0 -100px;
    border-radius: 50%;
    background: var(--seal-white);
    display: flex;
    align-items: center;
    justify-content: center;
    text-align: center;
  }
  .hospital-seal-name {
    font-family: "Roboto Slab", Georgia, serif;
    font-weight: 700;
    font-size: 25px;
    line-height: 1.15;
    color: var(--card-navy);
  }

  .doctor-name {
    position: absolute;
    left: 42px;
    top: 62px;
    font-family: "Roboto Slab", Georgia, serif;
    font-weight: 700;
    font-size: 31px;
    line-height: 1.18;
  }
  .doctor-role {
    position: absolute;
    left: 42px;
    top: 222px;
    font-size: 14px;
    line-height: 1.25;
    color: var(--accent-yellow);
  }
  .office-hours {
    position: absolute;
    left: 42px;
    top: 264px;
    font-size: 12.5px;
  }
  .contact-block {
    position: absolute;
    left: 42px;
    top: 370px;
    font-size: 14.5px;
    line-height: 1.4;
  }
  .label {
    font-weight: 700;
    color: var(--accent-yellow);
  }
  .note {
    font-size: 12px;
    color: var(--accent-yellow);
  }
  .indent { padding-left: 16px; }
  .address-block {
    position: absolute;
    left: 42px;
    top: 530px;
    font-size: 14.5px;
    line-height: 1.35;
  }
  .language-note {
    position: absolute;
    right: 16px;
    top: 340px;
    font-size: 13px;
    writing-mode: vertical-rl;
  }
</style>
</head>
<body>
<main class="canvas">
  <section class="card card-front" aria-label="Anverso de la tarjeta">
    <div class="hospital-seal">
      <span class="hospital-seal-name">Hospital<br>Almendral</span>
    </div>
  </section>

  <section class="card card-back" aria-label="Reverso de la tarjeta">
    <h1 class="doctor-name">Dr. Mateo<br>Anselmo<br>Quiroga<br>Benítez</h1>
    <p class="doctor-role">Medicina general<br>(Hospital Almendral)</p>
    <p class="office-hours">Sábado y domingo 10:00 am a 10:00 pm</p>

    <div class="contact-block">
      <p><span class="label">Tel:</span> 471-5836</p>
      <p class="indent">613-907-5148 <span class="note">(Emergencias)</span></p>
      <p><span class="label">E-mail:</span> mateoqb@correoandino.net</p>
    </div>

    <p class="address-block"><span class="label">Address:</span> Calle Tomás Ibarrola<br>#527 Col. Peñascal</p>

    <p class="language-note">English Spoken</p>
  </section>
</main>
</body>
</html>
```